Wordpress Website for electrician

I'm looking for an easy to maintain website for my electrical contracting business. Need a professional and appealing site.
Im wanting a website where clients can come on and look at services we offer, case studies and advertise our services.
Colours I'm wanting to incorporate are green, white, black and grey
I'm wanting a big slide show on main page where I can place advertising etc.
Menu is to include home, services, our work, specials, energy efficiency and contact
My existing site is www.trelwirefix.com.au
Updates
looking for something with a similar layout to this website
Target Market(s)
Businesses
Industry/Entity Type
Electrician
Look and feel

```html
<!DOCTYPE html>
<html lang="en">
<head>
<meta charset="utf-8">
<title>Trelwirefix – Electrical Contractor</title>
<link href="https://fonts.googleapis.com/css2?family=Oswald:wght@400;500&family=Open+Sans:wght@400;600;700&family=PT+Sans:wght@700&display=swap" rel="stylesheet">
<style>
:root{
  --green:#3dbb3c;
  --green-text:#3aaa35;
  --ink:#1d1d1d;
  --body-text:#333;
  --grey-nav:#6a6a6a;
  --grey-band:#e3e3e3;
  --grey-box:#d3d3d3;
  --grey-foot:#9c9c9c;
  --page:#efefef;
  --white:#fff;
}
*{margin:0;padding:0;box-sizing:border-box}
html,body{width:934px;height:1200px;overflow:hidden}
body{background:var(--page);font-family:"Open Sans",Arial,sans-serif;color:var(--body-text);position:relative}
.abs{position:absolute}

/* header */
.brand{left:78px;top:14px;display:flex;align-items:center;gap:10px}
.brand-dot{width:34px;height:34px;border-radius:50%;background:var(--green)}
.brand-name{font-family:"Open Sans",Arial,sans-serif;font-weight:700;font-size:26px;color:var(--ink)}
.brand-sub{left:166px;top:42px;font-size:8px;color:#888}
.contact-list{left:674px;top:9px;list-style:none}
.contact-list li{display:flex;align-items:center;gap:10px;height:19px;font-family:"Oswald",sans-serif;font-size:12.5px;color:#666;letter-spacing:.2px}
.contact-list svg{width:16px;height:12px}

/* nav */
.main-nav{left:78px;top:72px;width:778px;height:26px;background:var(--green);display:flex}
.main-nav a{display:block;height:26px;line-height:26px;color:var(--white);font-family:"Oswald",sans-serif;font-size:9.5px;text-decoration:none;letter-spacing:.4px;padding:0 19px 0 21px}
.main-nav a.active{background:var(--grey-nav)}

/* slider */
.hero{left:78px;top:98px;width:778px;height:247px;background:linear-gradient(180deg,#0a2140 0%,#133a67 45%,#0c2648 100%);overflow:hidden}
.hero-band{left:0;top:46px;width:778px;height:150px;background:rgba(6,24,50,.55)}
.hero-text{left:0;top:80px;width:778px;text-align:center;font-family:"PT Sans",sans-serif;font-weight:700;font-size:22px;line-height:28px;color:var(--white);text-shadow:0 1px 3px rgba(0,0,0,.6)}
.hero-arrow{top:101px;width:36px;height:36px;border-radius:50%;background:linear-gradient(#fff,#ddd);box-shadow:0 1px 4px rgba(0,0,0,.5);display:flex;align-items:center;justify-content:center}
.hero-arrow svg{width:12px;height:14px;fill:#555}
.hero-dots{left:308px;top:221px;display:flex;gap:3.5px}
.hero-dots span{width:12px;height:12px;border-radius:50%;background:linear-gradient(#fff,#c8c8c8);box-shadow:0 0 2px rgba(0,0,0,.5)}

/* services */
.service{top:354px;width:231px}
.service-photo{width:231px;height:111px;box-shadow:0 6px 8px -4px rgba(0,0,0,.45)}
.service h3{margin-top:14px;text-align:center;font-family:"Oswald",sans-serif;font-weight:400;font-size:15px;color:var(--ink);letter-spacing:-.4px}
.service p{margin:3px 2px 0 5px;font-size:8px;line-height:11px;color:#333;letter-spacing:-.1px}

/* main panel */
.feature-panel{left:78px;top:540px;width:778px;height:335px;background:var(--white);box-shadow:0 1px 3px rgba(0,0,0,.3)}
.promo{left:12px;width:470px}
.promo h2{font-family:"Oswald",sans-serif;font-weight:400;font-size:19px;line-height:26px;color:var(--green-text);letter-spacing:-.6px;text-transform:uppercase}
.promo p{margin-top:12px;font-size:8.3px;line-height:15px;color:#333}
.btn{height:19px;line-height:17px;border-radius:3px;font-family:"Oswald",sans-serif;font-size:9.5px;color:var(--white);text-align:center;letter-spacing:.3px;border:1px solid rgba(0,0,0,.35)}
.btn-green{background:linear-gradient(#7fd86c,#3bb03a)}
.btn-dark{background:linear-gradient(#555,#222)}
.ad-column{left:505px;top:0;width:273px;height:335px;box-shadow:-4px 0 6px -4px rgba(0,0,0,.3)}
.ad-picture{left:115px;top:12px;width:36px;height:62px;background:linear-gradient(#d8e6cc,#e6e6e6)}
.ad-headline{left:0;top:76px;width:273px;text-align:center;font-family:"Open Sans",sans-serif;font-weight:700;line-height:36px}
.ad-headline .g{font-size:41px;color:var(--green-text)}
.ad-headline .k{font-size:32px;color:var(--ink)}
.ad-grass{left:8px;top:178px;width:256px;height:24px;background:linear-gradient(#7ccc3a,#2f8a1c)}
.special{left:8px;top:212px;width:256px;height:110px;background:linear-gradient(#f4f4f4,#e4e4e4);overflow:hidden}
.special-photo{left:28px;top:14px;width:80px;height:84px;background:linear-gradient(135deg,#9a7dc0,#d9d9d9)}
.special-ribbon{left:0;top:0;width:60px;height:60px}
.special h4{left:97px;top:6px;font-family:"Oswald",sans-serif;font-weight:500;font-size:17px;color:var(--green-text)}
.special .sub{left:126px;top:28px;font-size:9px;font-weight:700;color:#222}
.special .price{left:124px;top:38px;font-family:"Open Sans",sans-serif;font-weight:700;font-size:38px;line-height:52px;color:#6ec96a}
.special .each{left:208px;top:49px;font-size:7px;font-weight:700;color:#6ec96a}
.special .more{left:117px;top:94px;font-size:8.5px;font-weight:700;color:var(--green-text)}
.special .cond{left:36px;top:98px;font-size:5.5px;font-weight:700;color:#222}

/* lower band */
.lower-band{left:0;top:888px;width:934px;height:254px;background:var(--grey-band);border-top:1px solid #d6d6d6}
.col-title{top:903px;font-family:"Oswald",sans-serif;font-weight:400;font-size:15px;color:var(--ink);letter-spacing:-.4px}
.col-title span{color:var(--green-text)}
.list-box{top:932px;width:250px;height:195px;background:var(--grey-box)}
.list-item{position:absolute;left:7px;width:236px;height:60px;border-bottom:1px solid #eee}
.list-thumb{position:absolute;left:0;top:6px;width:58px;height:40px}
.list-item h5{position:absolute;left:68px;top:4px;font-size:8.3px;font-weight:400;color:var(--green-text)}
.list-item h5 em{color:#333}
.list-item p{position:absolute;left:68px;top:17px;width:166px;font-size:8.3px;line-height:11.5px;color:#333}
.view-more{position:absolute;right:8px;bottom:6px;font-size:8px;color:var(--green-text)}
.accredit{left:630px;top:932px;width:210px;text-align:center;font-family:"Oswald",sans-serif;font-weight:400;font-size:14px;line-height:17px;color:var(--ink)}
.badge{left:620px;top:985px;width:226px;height:140px}

/* footer */
.site-footer{left:0;top:1142px;width:934px;height:58px;background:var(--grey-foot);color:var(--white);text-align:center}
.site-footer p{margin-top:14px;font-size:7.5px}
.footer-nav{display:flex;justify-content:center;margin-top:8px}
.footer-nav a{color:var(--white);text-decoration:none;font-size:8px;font-weight:600;padding:0 17px}
</style>
</head>
<body>

<header>
  <div class="abs brand"><span class="brand-dot"></span><span class="brand-name">trelwirefix</span></div>
  <div class="abs brand-sub">electrical contractor</div>
  <ul class="abs contact-list">
    <li><svg viewBox="0 0 16 12"><path d="M0 0h16v12H0z" fill="#333"/><path d="M1 1l7 6 7-6" stroke="#eee" stroke-width="1.2" fill="none"/></svg>INFO@TRELWIREFIX.COM.AU</li>
    <li><svg viewBox="0 0 16 12"><path d="M0 0h16v12H0z" fill="#333"/><path d="M1 1l7 6 7-6" stroke="#eee" stroke-width="1.2" fill="none"/></svg>SALES@TRELWIREFIX.COM.AU</li>
    <li><svg viewBox="0 0 16 12"><rect x="5" y="0" width="7" height="12" rx="1" fill="#333"/><rect x="6.2" y="1.5" width="4.6" height="7" fill="#eee"/></svg>MOBILE: 0400 555 018</li>
  </ul>
</header>

<nav class="abs main-nav">
  <a href="#">HOME</a><a href="#" class="active">SERVICES</a><a href="#">OUR WORK</a><a href="#">SPECIALS</a><a href="#">ENERGY EFFICIENCY</a><a href="#">CONTACT</a>
</nav>

<section class="abs hero" role="img" aria-label="Slide photo of two cut electrical cables with sparks arcing between them">
  <div class="abs hero-band"></div>
  <p class="abs hero-text">Every job we do, we take the same approach.<br>To be professional, tidy, deliver a great workmanship<br>and most importantly make the customer happy.</p>
  <div class="abs hero-arrow" style="left:5px"><svg viewBox="0 0 12 14"><path d="M10 0L2 7l8 7z"/></svg></div>
  <div class="abs hero-arrow" style="left:737px"><svg viewBox="0 0 12 14"><path d="M2 0l8 7-8 7z"/></svg></div>
  <div class="abs hero-dots"><span></span><span></span><span></span><span></span><span></span><span></span><span></span><span></span><span></span><span></span></div>
</section>

<section>
  <article class="abs service" style="left:78px">
    <div class="service-photo" role="img" aria-label="Photo of cable trays with bundled wiring" style="background:linear-gradient(135deg,#a8a49a,#c57a2c 50%,#6e6a60)"></div>
    <h3>ELECTRICAL CONTRACTING</h3>
    <p>We offer all types of electrical work from Installation to maintenance</p>
  </article>
  <article class="abs service" style="left:352px">
    <div class="service-photo" role="img" aria-label="Aerial photo of a roof covered in solar panels" style="background:linear-gradient(160deg,#6d7a88,#2d3a52 45%,#c9c9c9 70%,#8b3a2c)"></div>
    <h3>ENERGY EFFICIENCY</h3>
    <p>With one of our audits to your business or home we can lower your energy bills and minimise your carbon footprint</p>
  </article>
  <article class="abs service" style="left:625px">
    <div class="service-photo" role="img" aria-label="Photo of a modern boardroom with a long table" style="background:linear-gradient(180deg,#1f3658,#2a4570 55%,#d6c79a 75%,#3a3a3a)"></div>
    <h3>UNDERGROUND LOCATING</h3>
    <p>We have the tools and knowledge in locating underground utilities.</p>
  </article>
</section>

<main class="abs feature-panel">
  <div class="abs promo" style="top:6px">
    <h2>LED is the future</h2>
    <p>LED lighting has involved rapidly in the last 5 years. In the coming years we will see all lighting being substitued with LED lights. It is by far the most efficient form of lighting on todays market. Let us retrofit your business or home with LED and the savings will literally pay the lights off.</p>
  </div>
  <a class="abs btn btn-green" style="left:285px;top:101px;width:95px">WHY LED</a>
  <a class="abs btn btn-dark" style="left:385px;top:101px;width:95px">REQUEST QOUTE</a>

  <div class="abs promo" style="top:147px">
    <h2>Reduce your business energy consumption</h2>
    <p>By letting us analyse your energy consumption, we can identify where you are simply burning your money. We can suggest and implement easy solutions to save you money and minimise your carbon emmissions.</p>
  </div>
  <a class="abs btn btn-green" style="left:245px;top:241px;width:133px">ENERGY EFFICIENCY AUDIT?</a>
  <a class="abs btn btn-dark" style="left:383px;top:241px;width:95px">BOOK AUDIT NOW</a>

  <aside class="abs ad-column">
    <div class="abs ad-picture" role="img" aria-label="Illustration of a light bulb with a small tree inside"></div>
    <div class="abs ad-headline"><div class="g">BE GREEN</div><div class="k">SAVE MONEY</div></div>
    <div class="abs ad-grass" role="img" aria-label="Strip of green grass"></div>
    <div class="abs special">
      <div class="abs special-photo" role="img" aria-label="Boxed LED downlight product"></div>
      <svg class="abs special-ribbon" viewBox="0 0 60 60"><path d="M0 34L34 0h18L0 52z" fill="#e01f26"/><text x="21.5" y="24.5" text-anchor="middle" transform="rotate(-45 21.5 21.5)" font-family="Oswald,sans-serif" font-size="8" fill="#fff">SPECIALS</text></svg>
      <h4 class="abs">LED DOWNLIGHTS</h4>
      <span class="abs sub">Supplied &amp; Installed</span>
      <span class="abs price">$33</span>
      <span class="abs each">EACH</span>
      <span class="abs cond">CONDITIONS APPLY</span>
      <span class="abs more">Click here for more details</span>
    </div>
  </aside>
</main>

<section class="abs lower-band"></section>

<h3 class="abs col-title" style="left:79px">LATEST <span>NEWS</span></h3>
<div class="abs list-box" style="left:79px">
  <div class="list-item" style="top:0"><div class="list-thumb" role="img" aria-label="Photo of glowing light bulbs" style="background:linear-gradient(135deg,#3a2a18,#d08a2a,#2a1c10)"></div><h5>Electricity Prices Soar</h5><p>The Australian government's carbon tax will see electricity prices soar</p></div>
  <div class="list-item" style="top:60px"><div class="list-thumb" role="img" aria-label="Photo of a lit bulb on a blue background" style="background:radial-gradient(circle,#cfe6ff,#1e4a8a 55%,#0b1f3c)"></div><h5>At Center of Oil Boom</h5><p>The Australian government's carbon tax will see electricity prices soar</p></div>
  <div class="list-item" style="top:120px;border:0"><div class="list-thumb" role="img" aria-label="Green power plug illustration" style="background:linear-gradient(135deg,#2f9a2a,#9ee07a)"></div><h5>Green Electricity</h5><p>The Australian government's carbon tax will see electricity prices soar</p></div>
  <a class="view-more">view more</a>
</div>

<h3 class="abs col-title" style="left:345px">CLIENT <span>TESTIMONIES</span></h3>
<div class="abs list-box" style="left:345px">
  <div class="list-item" style="top:0"><div class="list-thumb" role="img" aria-label="Client portrait photo" style="background:linear-gradient(135deg,#8fa8c8,#e0e0e0)"></div><h5>Dean Harlow <em>- Norvane Group</em></h5><p>Trelwirefix considerd all our needs and incorparated energy saving</p></div>
  <div class="list-item" style="top:60px"><div class="list-thumb" role="img" aria-label="Client portrait photo" style="background:linear-gradient(135deg,#8fa8c8,#e0e0e0)"></div><h5>Dean Harlow <em>- Norvane Group</em></h5><p>Trelwirefix considerd all our needs and incorparated energy saving</p></div>
  <div class="list-item" style="top:120px;border:0"><div class="list-thumb" role="img" aria-label="Client portrait photo" style="background:linear-gradient(135deg,#8fa8c8,#e0e0e0)"></div><h5>Dean Harlow <em>- Norvane Group</em></h5><p>Trelwirefix considerd all our needs and incorparated energy saving</p></div>
  <a class="view-more">view more</a>
</div>

<h3 class="abs accredit">PROUDLY ACCREDITED<br>GREENWISE ELECTRICIANS</h3>
<svg class="abs badge" viewBox="0 0 226 140" role="img" aria-label="Accreditation badge"><rect x="48" y="8" width="130" height="124" rx="12" fill="#cfd8cf"/></svg>

<footer class="abs site-footer">
  <p>Trelwirefix is a Registered Electrical Contractor - REC. 48102</p>
  <nav class="footer-nav"><a href="#">Home</a><a href="#">Services</a><a href="#">Our Work</a><a href="#">Specials</a><a href="#">Energy Efficiency</a><a href="#">Contact</a></nav>
</footer>

</body>
</html>
```